Geschäftspapier für Cateringunternehmen
Zielgruppe
Wir werden ein neues Unternehmen im Bereich Catering.
Aufgabenstellung
Wir benötigen Briefpapier und Visitenkarten.
Auf den Visitenkarten sollen folgende Angaben stehen: LOGO und unten: Mira Kessler - Inhaberin Telefon: 0351-4836150 , Jonas Wolfart - Küchenchef Telefon: +49 172 6381742
Lindenweg 14, 01259 Dresden, Mail: info@tafelglanz-beispiel.de, www.tafelglanz-beispiel.de
Wenn es auf den Briefbogen und Visitenkarte passt: Wir machen Ihr perfektes Catering für Hochzeiten, Firmenfeiern, Geburtstage und sonstige Events! (oder vielleicht haben die Designer noch tolle Ideen - wir fertigen Caterings für jeden Anlass!)

```html
<!DOCTYPE html>
<html lang="de">
<head>
<meta charset="utf-8">
<title>Tafelglanz – Geschäftsausstattung</title>
<link rel="stylesheet" href="https://fonts.googleapis.com/css2?family=Libre+Baskerville:wght@400;700&family=Montserrat:wght@500&family=Open+Sans:wght@400&display=swap">
<style>
  :root {
    --ink: #0a0a0a;
    --paper: #ffffff;
    --shadow: rgba(0,0,0,0.55);
    --muted: #d9d9d9;
  }
  * { margin: 0; padding: 0; box-sizing: border-box; }
  html, body { width: 1200px; height: 1121px; overflow: hidden; background: var(--paper); }
  .canvas { position: relative; width: 1200px; height: 1121px; background: var(--paper); }

  .sheet { position: absolute; background: var(--paper); box-shadow: 10px 9px 9px var(--shadow); }

  .brand {
    position: absolute; display: flex; align-items: center; gap: 4px;
    font-family: "Libre Baskerville", serif; font-weight: 700;
    color: var(--ink); letter-spacing: 0.02em; white-space: nowrap;
    transform: translate(-50%, -50%);
  }
  .brand .dot { border: 1.5px solid currentColor; border-radius: 50%; flex: none; }
  .brand.on-dark { color: var(--paper); }

  .tagline {
    position: absolute; transform: translateX(-50%);
    font-family: "Libre Baskerville", serif; font-variant: small-caps; font-weight: 700;
    text-align: center; white-space: nowrap; line-height: 1.6;
  }

  .contact { position: absolute; font-family: "Montserrat", sans-serif; font-weight: 500; white-space: nowrap; }
  .contact .item { position: absolute; display: flex; align-items: center; }
  .icon { fill: currentColor; flex: none; }
  .lines { line-height: 1.2; letter-spacing: 0.06em; }

  /* compliment slip */
  .slip { left: 44px; top: 92px; width: 473px; height: 206px; }

  /* envelope */
  .envelope { left: 36px; top: 378px; width: 482px; height: 205px; box-shadow: -10px 9px 9px var(--shadow); }
  .envelope-flap { position: absolute; left: 36px; top: 321px; width: 482px; height: 58px; }
  .envelope .contact { color: var(--ink); font-size: 5px; }

  /* business cards */
  .card-front { left: 62px; top: 655px; width: 305px; height: 181px; border-radius: 6px; }
  .card-back { left: 57px; top: 869px; width: 306px; height: 184px; border-radius: 6px; background: var(--ink); color: var(--paper); }
  .people { position: absolute; left: 37px; top: 81px; font-family: "Libre Baskerville", serif; }
  .person-name { font-size: 9.5px; font-weight: 400; letter-spacing: 0.01em; }
  .person-role { font-size: 4px; letter-spacing: 0.06em; margin-top: 1px; margin-bottom: 4px; }
  .divider { position: absolute; left: 153px; top: 66px; width: 1px; height: 72px; background: var(--paper); }
  .card-back .contact { font-size: 5.2px; color: var(--paper); }

  /* letterhead */
  .letterhead { left: 570px; top: 85px; width: 596px; height: 750px; }
  .signature { position: absolute; left: 433px; top: 589px; font-family: "Open Sans", sans-serif; font-size: 20px; color: var(--ink); }
  .signature-line { position: absolute; left: 433px; top: 630px; width: 92px; height: 1.5px; background: var(--ink); }
  .letter-footer { position: absolute; left: 0; bottom: 0; width: 100%; height: 41px; background: var(--ink); color: var(--paper); }
  .letter-footer .contact { font-size: 7px; color: var(--paper); }
</style>
</head>
<body>
<svg width="0" height="0" style="position:absolute" aria-hidden="true">
  <symbol id="i-phone" viewBox="0 0 24 24"><path d="M6.6 10.8a15 15 0 0 0 6.6 6.6l2.2-2.2a1 1 0 0 1 1-.25 11.4 11.4 0 0 0 3.6.6 1 1 0 0 1 1 1V20a1 1 0 0 1-1 1A17 17 0 0 1 3 4a1 1 0 0 1 1-1h3.5a1 1 0 0 1 1 1c0 1.25.2 2.45.57 3.57a1 1 0 0 1-.25 1z"/></symbol>
  <symbol id="i-pin" viewBox="0 0 24 24"><path d="M12 2a7 7 0 0 0-7 7c0 5.25 7 13 7 13s7-7.75 7-13a7 7 0 0 0-7-7zm0 9.5A2.5 2.5 0 1 1 12 6.5a2.5 2.5 0 0 1 0 5z"/></symbol>
  <symbol id="i-mail" viewBox="0 0 24 24"><path d="M2 5h20v14H2zm2 2v.5l8 5 8-5V7l-8 5z"/></symbol>
  <symbol id="i-globe" viewBox="0 0 24 24"><path d="M12 2a10 10 0 1 0 0 20 10 10 0 0 0 0-20zm6.9 6h-3a15 15 0 0 0-1.3-3.6A8 8 0 0 1 18.9 8zM12 4a14 14 0 0 1 1.9 4h-3.8A14 14 0 0 1 12 4zM4.3 14a8 8 0 0 1 0-4h3.4a16 16 0 0 0 0 4zm.8 2h3a15 15 0 0 0 1.3 3.6A8 8 0 0 1 5.1 16zm3-8h-3a8 8 0 0 1 4.3-3.6A15 15 0 0 0 8.1 8zM12 20a14 14 0 0 1-1.9-4h3.8A14 14 0 0 1 12 20zm2.3-6H9.7a14 14 0 0 1 0-4h4.6a14 14 0 0 1 0 4zm.3 5.6a15 15 0 0 0 1.3-3.6h3a8 8 0 0 1-4.3 3.6zm1.7-5.6a16 16 0 0 0 0-4h3.4a8 8 0 0 1 0 4z"/></symbol>
</svg>

<main class="canvas">

  <!-- compliment slip -->
  <section class="sheet slip">
    <div class="brand" style="left:82px; top:60px; font-size:10px;"><span class="dot" style="width:8px;height:8px;"></span>TAFELGLANZ</div>
  </section>

  <!-- envelope -->
  <svg class="envelope-flap" viewBox="0 0 482 58" aria-hidden="true">
    <path d="M0 58 L7 12 Q9 0 26 0 L456 0 Q473 0 475 12 L482 58 Z" fill="var(--ink)"/>
  </svg>
  <div class="brand on-dark" style="left:277px; top:350px; font-size:10px;"><span class="dot" style="width:8px;height:8px;"></span>TAFELGLANZ</div>
  <section class="sheet envelope">
    <div class="contact" style="left:0; top:0;">
      <div class="item" style="left:24px; top:181px;"><svg class="icon" width="6" height="6"><use href="#i-phone"/></svg></div>
      <div class="item lines" style="left:38px; top:180px;">Inhaberin &nbsp;&nbsp;: 0351-4836150<br>Küchenchef : +49 172 6381742</div>
      <div class="item" style="left:146px; top:181px;"><svg class="icon" width="6" height="7"><use href="#i-pin"/></svg></div>
      <div class="item" style="left:161px; top:183px;">Lindenweg 14, 01259 Dresden</div>
      <div class="item" style="left:253px; top:182px;"><svg class="icon" width="6" height="6"><use href="#i-mail"/></svg></div>
      <div class="item" style="left:268px; top:183px;">info@tafelglanz-beispiel.de</div>
      <div class="item" style="left:361px; top:182px;"><svg class="icon" width="6" height="6"><use href="#i-globe"/></svg></div>
      <div class="item" style="left:375px; top:183px;">www.tafelglanz-beispiel.de</div>
    </div>
  </section>

  <!-- business card front -->
  <section class="sheet card-front">
    <div class="brand" style="left:152px; top:89px; font-size:19px; gap:7px;"><span class="dot" style="width:14px;height:14px;border-width:2px;"></span>TAFELGLANZ</div>
  </section>

  <!-- business card back -->
  <section class="sheet card-back">
    <div class="brand on-dark" style="left:153px; top:34px; font-size:10.5px;"><span class="dot" style="width:8px;height:8px;"></span>TAFELGLANZ</div>
    <div class="people">
      <div class="person-name">MIRA KESSLER</div>
      <div class="person-role">INHABERIN</div>
      <div class="person-name">JONAS WOLFART</div>
      <div class="person-role">KÜCHENCHEF</div>
    </div>
    <div class="divider"></div>
    <div class="contact" style="left:0; top:0;">
      <div class="item" style="left:164px; top:75px;"><svg class="icon" width="6" height="6"><use href="#i-phone"/></svg></div>
      <div class="item lines" style="left:180px; top:73px;">Inhaberin &nbsp;&nbsp;: 0351-4836150<br>Küchenchef : +49 172 6381742</div>
      <div class="item" style="left:164px; top:93px;"><svg class="icon" width="6" height="7"><use href="#i-pin"/></svg></div>
      <div class="item" style="left:180px; top:94px;">Lindenweg 14, 01259 Dresden</div>
      <div class="item" style="left:164px; top:109px;"><svg class="icon" width="6" height="6"><use href="#i-mail"/></svg></div>
      <div class="item" style="left:180px; top:109px;">info@tafelglanz-beispiel.de</div>
      <div class="item" style="left:164px; top:124px;"><svg class="icon" width="6" height="6"><use href="#i-globe"/></svg></div>
      <div class="item" style="left:180px; top:124px;">www.tafelglanz-beispiel.de</div>
    </div>
    <p class="tagline" style="left:153px; top:155px; font-size:4px; color:var(--paper);">Wir machen Ihr perfektes Catering für Hochzeiten, Firmenfeiern,<br>Geburtstage und sonstige Events!</p>
  </section>

  <!-- letterhead -->
  <section class="sheet letterhead">
    <div class="brand" style="left:298px; top:73px; font-size:14px; gap:5px;"><span class="dot" style="width:11px;height:11px;"></span>TAFELGLANZ</div>
    <p class="tagline" style="left:298px; top:110px; font-size:5.2px; color:var(--ink);">Wir machen Ihr perfektes Catering für Hochzeiten, Firmenfeiern,<br>Geburtstage und sonstige Events!</p>
    <div class="signature">Signature</div>
    <div class="signature-line"></div>
    <footer class="letter-footer">
      <div class="contact" style="left:0; top:0;">
        <div class="item" style="left:14px; top:16px;"><svg class="icon" width="8" height="8"><use href="#i-phone"/></svg></div>
        <div class="item lines" style="left:34px; top:11px;">Inhaberin &nbsp;&nbsp;: 0351-4836150<br>Küchenchef : +49 172 6381742</div>
        <div class="item" style="left:174px; top:14px;"><svg class="icon" width="8" height="10"><use href="#i-pin"/></svg></div>
        <div class="item" style="left:192px; top:16px; letter-spacing:0.05em;">Lindenweg 14, 01259 Dresden</div>
        <div class="item" style="left:313px; top:16px;"><svg class="icon" width="9" height="8"><use href="#i-mail"/></svg></div>
        <div class="item" style="left:333px; top:16px; letter-spacing:0.05em;">info@tafelglanz-beispiel.de</div>
        <div class="item" style="left:453px; top:16px;"><svg class="icon" width="8" height="8"><use href="#i-globe"/></svg></div>
        <div class="item" style="left:474px; top:16px; letter-spacing:0.05em;">www.tafelglanz-beispiel.de</div>
      </div>
    </footer>
  </section>

</main>
</body>
</html>
```